Employment and Trade Show Banner for Senior Living Solutions

We are looking to create a new sign for employment fairs and trade shows to promote our senior living campus and attract potential employees as well positively promote our campus to potential residents/tenants. We serve a variety of seniors at a variety of different care levels including: long-term care, rehabilitation, locked dementia care unit, assisted living, and independent living. The sign dimensions are 33" x 80". Our website is www.pinegrovelakeshore.com.

We are looking for something catchy and professional.

Our Vision: MapleRest of Dunmore offers a variety of senior services which include: Independent Living, Assisted Living, Rehabilitative Care, Skilled Nursing Care, and Memory Care. Our team provides the quality services you should expect in senior care.

Our Campus is made up of 4 different facilities: Ridgefell Care Center, LarchMeadow Village, Juniper Lodge, and Willowmere Court. Perhaps advertising these somehow under our umbrella name of MapleRest of Dunmore?

Target Market(s)

Attract potential employees as well positively promote our campus to potential residents/tenants who may need care in the future.

Industry/Entity Type

Trade

Requirements
Must have
• Logo
Nice to have
• Our Campus is made up of 4 different facilities: Ridgefell Care Center, LarchMeadow Village, Juniper Lodge, and Willowmere Court. Perhaps advertising these somehow under our umbrella name of MapleRest of Dunmore?
• Perhaps something based around our vision?
• Our Vision: MapleRest of Dunmore offers a variety of senior services which include: Independent Living, Assisted Living, Rehabilitative Care, Skilled Nursing Care, and Memory Care. Our team provides the quality services you should expect in senior care.

```html
<!DOCTYPE html>
<html lang="en">
<head>
<meta charset="utf-8">
<title>MapleRest of Dunmore – Banner</title>
<link href="https://fonts.googleapis.com/css2?family=Open+Sans:wght@400;600;700&display=swap" rel="stylesheet">
<style>
  :root {
    --forest: #0f6a33;
    --brand-green: #1b6b2a;
    --accent-orange: #e0701e;
    --ink: #2a2a2a;
    --body-text: #444444;
    --rule: #9a9a9a;
    --backdrop: #eceeef;
    --paper: #ffffff;
  }
  html, body {
    margin: 0;
    padding: 0;
    width: 1200px;
    height: 960px;
    overflow: hidden;
    background: var(--backdrop);
    font-family: "Open Sans", Arial, sans-serif;
  }
  .banner {
    position: absolute;
    left: 410px;
    top: 20px;
    width: 400px;
    height: 968px;
    background: var(--paper);
    transform: scale(0.95);
    transform-origin: top left;
    overflow: hidden;
    box-shadow: 0 2px 10px rgba(0,0,0,0.12);
  }
  .banner-art {
    position: absolute;
    inset: 0;
    width: 400px;
    height: 968px;
  }
  .text { position: absolute; left: 0; width: 400px; text-align: center; margin: 0; }
  .brand-name {
    top: 108px;
    font-size: 22px;
    font-weight: 600;
    color: var(--forest);
    letter-spacing: 0.5px;
  }
  .headline {
    top: 170px;
    font-size: 25px;
    font-weight: 400;
    line-height: 26px;
    color: var(--ink);
  }
  .intro {
    top: 578px;
    font-size: 15px;
    line-height: 18px;
    color: var(--body-text);
  }
  .services { position: absolute; left: 0; top: 0; width: 400px; }
  .service {
    position: absolute;
    font-size: 13px;
    font-weight: 600;
    line-height: 14px;
    color: var(--brand-green);
    text-align: center;
  }
  .tagline {
    top: 716px;
    font-size: 19.5px;
    font-weight: 700;
    color: var(--accent-orange);
    letter-spacing: 0.2px;
  }
  .about {
    top: 753px;
    left: 20px;
    width: 360px;
    font-size: 11px;
    line-height: 14.6px;
    color: var(--body-text);
  }
  .website {
    top: 826px;
    font-size: 19px;
    font-weight: 700;
    color: var(--ink);
  }
  .website svg { vertical-align: -2px; margin-right: 8px; }
</style>
</head>
<body>
  <div class="banner">
    <svg class="banner-art" viewBox="0 0 400 968" xmlns="http://www.w3.org/2000/svg">
      <defs>
        <clipPath id="arch-clip">
          <circle cx="200" cy="293" r="260"/>
        </clipPath>
        <linearGradient id="hero-tones" x1="0" y1="0" x2="1" y2="1">
          <stop offset="0" stop-color="#d9cfc7"/>
          <stop offset="0.45" stop-color="#9a8f88"/>
          <stop offset="0.75" stop-color="#e9e4df"/>
          <stop offset="1" stop-color="#bfb3ad"/>
        </linearGradient>
        <linearGradient id="hands-tones" x1="0" y1="0" x2="1" y2="1">
          <stop offset="0" stop-color="#b79c8e"/>
          <stop offset="1" stop-color="#7d7470"/>
        </linearGradient>
      </defs>
      <rect class="header-band" x="0" y="0" width="400" height="150" fill="var(--forest)"/>
      <circle class="header-arch" cx="200" cy="293" r="260" fill="var(--paper)"/>
      <g clip-path="url(#arch-clip)">
        <rect x="0" y="235" width="400" height="330" fill="url(#hero-tones)" role="img" aria-label="Photo of a smiling young caregiver leaning beside a senior woman seated in a wheelchair"/>
      </g>
      <circle class="dot" cx="343" cy="81" r="13" fill="var(--paper)"/>
      <circle class="dot" cx="63" cy="520" r="21" fill="var(--accent-orange)"/>
      <!-- service grid rules -->
      <line x1="129" y1="628" x2="129" y2="664" stroke="var(--rule)" stroke-width="1"/>
      <line x1="260" y1="628" x2="260" y2="664" stroke="var(--rule)" stroke-width="1"/>
      <line x1="29" y1="667" x2="367" y2="667" stroke="var(--rule)" stroke-width="1.2"/>
      <line x1="189" y1="667" x2="189" y2="703" stroke="var(--rule)" stroke-width="1"/>
      <!-- footer photo -->
      <circle cx="286" cy="958" r="88" fill="url(#hands-tones)" role="img" aria-label="Close-up photo of a senior's hands resting on a walking cane"/>
      <circle class="dot" cx="200" cy="926" r="13" fill="var(--accent-orange)"/>
    </svg>

    <p class="text brand-name">MapleRest of Dunmore</p>
    <h1 class="text headline">Creatively providing<br>a caring community</h1>
    <p class="text intro">We serve a variety of seniors at a variety of<br>different care levels including</p>

    <div class="services">
      <div class="service" style="left:22px;width:106px;top:631px;">Skilled Nursing<br>Care</div>
      <div class="service" style="left:130px;width:130px;top:631px;">Short Term<br>Rehabilitative Care</div>
      <div class="service" style="left:262px;width:110px;top:631px;">Secure Memory<br>Care</div>
      <div class="service" style="left:55px;width:120px;top:674px;">Assisted Living<br>Communities</div>
      <div class="service" style="left:200px;width:120px;top:674px;">Independent<br>Senior Living</div>
    </div>

    <p class="text tagline">CREATIVE . CARING . COMMUNITIES</p>
    <p class="text about">MapleRest of Dunmore consists of four Communities offering a variety of neighborhoods for senior living. Each of these communities offers services along with compassionate, caring environments to meet each of our resident's needs.</p>
    <p class="text website"><svg width="14" height="14" viewBox="0 0 14 14" aria-hidden="true"><g fill="none" stroke="var(--brand-green)" stroke-width="1.2"><circle cx="7" cy="7" r="6"/><ellipse cx="7" cy="7" rx="2.6" ry="6"/><line x1="1" y1="7" x2="13" y2="7"/><line x1="2" y1="4" x2="12" y2="4"/><line x1="2" y1="10" x2="12" y2="10"/></g></svg>www.pinegrovelakeshore.com</p>
  </div>
</body>
</html>
```